Your conflict - our mediation - joint conflict SOLUTION

With this flyer I am looking for conflict parties who are ready to tackle and resolve their conflict with a prospective mediator. The mediation is free because I am doing it as part of my diploma thesis. Time frame approx. 4 sessions of 2.5 hours each. The wishes and needs of both parties are listened to and “picked out”. In an open, constructive, appreciative framework, solutions are developed and negotiated together.

Target Market(s)

everyone who is ready to deal with himself and his counterpart and everyone who wants to work out a solution with the respect, openness and support of a mediator.

Requirements
Must have
• - "For my diploma thesis I am looking for conflicting parties who are willing to resolve their conflict with a mediator"
- Time frame: 4 x 2.5 hours feasible in Solothurn, Bern, Brugg
- Free of charge
- my coordinates - see business card
- more information at www.lindenhofwerk.ch
Nice to have
• the card should be based on the style of my homepage www.lindenhofwerk.ch and my business card

```html
<!DOCTYPE html>
<html lang="en">
<head>
<meta charset="utf-8">
<title>Mediation Flyer – Lindenhofwerk</title>
<link href="https://fonts.googleapis.com/css2?family=Montserrat:wght@500;600;700;800&display=swap" rel="stylesheet">
<style>
  :root {
    --page-bg: #5a5a5a;
    --paper: #eeeef2;
    --plum-dark: #3f2a52;
    --plum-mid: #745b8b;
    --plum-soft: #7a6393;
    --white: #ffffff;
    --ink: #3a2550;
    --photo-a: #d9d6dc;
    --photo-b: #8a8290;
  }
  * { margin: 0; padding: 0; box-sizing: border-box; }
  html, body { width: 1029px; height: 1200px; overflow: hidden; }
  body {
    background: var(--page-bg);
    font-family: "Montserrat", sans-serif;
    position: relative;
  }
  .flyer {
    position: absolute;
    left: 70px; top: 25px;
    width: 889px; height: 1150px;
    background: var(--paper);
    overflow: hidden;
  }
  .abs { position: absolute; }

  .photo {
    left: 348px; top: 35px; width: 541px; height: 533px;
    background: linear-gradient(135deg, var(--photo-a) 0%, #b7b1bb 45%, var(--photo-b) 100%);
  }

  .brand {
    left: 56px; top: 100px; width: 300px;
    display: flex; align-items: center; gap: 12px;
  }
  .brand-dot {
    width: 34px; height: 34px; border-radius: 50%;
    background: var(--plum-mid); flex: none;
  }
  .brand-name {
    font-weight: 700; font-size: 33px; color: var(--plum-mid);
    letter-spacing: 0.5px;
  }

  .headline-top {
    left: 58px; top: 268px;
    font-weight: 800; font-size: 58px; line-height: 1;
    color: var(--plum-mid); letter-spacing: -0.5px;
  }
  .stuck-box {
    left: 58px; top: 334px; width: 288px; height: 72px;
    background: var(--plum-dark);
    display: flex; align-items: center; justify-content: center;
    font-weight: 800; font-size: 58px; color: var(--white);
  }
  .divider-h {
    left: 64px; top: 437px; width: 287px; height: 2px;
    background: var(--plum-dark);
  }
  .need-line {
    left: 62px; top: 458px;
    font-weight: 700; font-size: 26px; color: var(--ink);
  }
  .mediator {
    left: 60px; top: 484px;
    font-weight: 800; font-size: 55px; color: var(--plum-dark);
    letter-spacing: -0.5px;
  }

  .band-free {
    left: 0; top: 568px; width: 889px; height: 107px;
    background: var(--plum-dark);
    display: flex; align-items: center; justify-content: center;
    font-weight: 800; font-size: 64px; color: var(--white);
    letter-spacing: 7px;
  }

  .details {
    left: 0; top: 675px; width: 889px; height: 381px;
    background: var(--plum-mid);
  }
  .intro {
    left: 0; top: 32px; width: 889px; text-align: center;
    font-weight: 500; font-size: 24px; line-height: 31px; color: var(--white);
  }
  .timeframe-label {
    left: 92px; top: 160px; width: 288px; height: 48px;
    background: var(--white);
    display: flex; align-items: center; justify-content: center;
    font-weight: 800; font-size: 31px; color: var(--plum-dark);
  }
  .hours {
    left: 92px; top: 218px;
    font-weight: 700; font-size: 36px; color: var(--white);
  }
  .places {
    left: 92px; top: 267px;
    font-weight: 500; font-size: 28px; line-height: 35px; color: var(--white);
  }
  .divider-v {
    left: 456px; top: 156px; width: 2px; height: 184px;
    background: var(--white);
  }
  .quote-frame { left: 505px; top: 140px; }
  .quote-text {
    left: 542px; top: 192px; width: 260px;
    font-weight: 500; font-size: 17px; line-height: 21px; color: var(--white);
  }

  .footer {
    left: 0; top: 1056px; width: 889px; height: 94px;
    background: var(--plum-dark);
    display: flex; align-items: center; justify-content: center;
    gap: 34px;
    font-weight: 500; font-size: 23px; color: var(--white);
  }
  .footer-sep { width: 2px; height: 24px; background: var(--white); }
</style>
</head>
<body>
  <main class="flyer">
    <div class="abs photo" role="img" aria-label="Photo of a woman and a man in a mediation session holding hands, a mediator taking notes on a clipboard"></div>

    <div class="abs brand">
      <span class="brand-dot"></span>
      <span class="brand-name">Lindenhofwerk</span>
    </div>

    <h1 class="abs headline-top">ARE YOU</h1>
    <div class="abs stuck-box">STUCK?</div>
    <div class="abs divider-h"></div>
    <p class="abs need-line">need conflict with a</p>
    <p class="abs mediator">MEDIATOR</p>

    <div class="abs band-free">FREE OF CHARGE</div>

    <section class="abs details">
      <p class="abs intro">For my diploma thesis I am looking for<br>conflicting parties who are willing to resolve their conflict<br>with a mediator</p>

      <div class="abs timeframe-label">TIME FRAME:</div>
      <p class="abs hours">4 x 2.5 hours</p>
      <p class="abs places">feasible in Solothurn,<br>Bern, Brugg</p>

      <div class="abs divider-v"></div>

      <svg class="abs quote-frame" width="320" height="240" viewBox="0 0 320 240" aria-hidden="true">
        <path d="M80 26 H305 V190 M235 190 H0 V26 H25" fill="none" stroke="#ffffff" stroke-width="1.6"/>
        <path d="M305 190 V196 H285" fill="none" stroke="#ffffff" stroke-width="1.6"/>
        <g fill="none" stroke="#ffffff" stroke-width="1.6">
          <path d="M30 6 C18 10 14 22 14 36 V54 H34 V34 H24 C24 24 28 16 36 12 Z"/>
          <path d="M56 6 C44 10 40 22 40 36 V54 H60 V34 H50 C50 24 54 16 62 12 Z"/>
          <path d="M244 196 H264 V214 C264 228 260 238 248 242 L242 236 C250 232 254 226 254 216 H244 Z"/>
          <path d="M270 196 H290 V214 C290 228 286 238 274 242 L268 236 C276 232 280 226 280 216 H270 Z"/>
        </g>
      </svg>
      <p class="abs quote-text">Because your own conflict makes you less able to think, feel and act, it is worthwhile to be accompanied by a mediator.</p>
    </section>

    <footer class="abs footer">
      <span>For More Information at</span>
      <span class="footer-sep"></span>
      <span>www.Lindenhofwerk.ch</span>
    </footer>
  </main>
</body>
</html>
```